For Sale Poster Design

We need a beautiful and tropical looking FOR SALE poster for our speed boat.

Poster format need to be 297x420mm / 300dpi
PSD with all layers.

The photos from the boat can be downloaded here: www.korvado.nl/photos.zip

Target Market(s)

Tourists, expats

Requirements
Must have
• The poster need to have the following text:

Speed Boat Sale

This beautiful full glass fiber speedboat (location Lombok, Indonesia) is perfect for tropical conditions: island transfer, diving, wake boarding, fishing, private charters and leisure activities.

The newly bought 2x 200 HP TORUMI 4 Stroke (2013) will give you an enormous power on the water with maximum speed of 40 Knot / 74 Km/hour. This will bring you from Lombok to Bali in just 50 minutes and only few minutes long from the famous tropical Gili islands.

The speedboat also has the comfort of a small cabin with skylight, sun controlled ventilation system, a small bed, a toilet and a fridge. There are 16 seats in the open section of the boat. The boat is equipped with modern brand-new GPS, Sonar and an FM / AM Radio system.

This speedboat was built in 2011 and is meticulously maintained to the highest standard. It comes with a captain and boatman.

Specs:
Overall length: 11 Meter 36 feet.
Built year: 2011, Bali
Engines: 2x 200 HP TORUMI 4 Stroke (Bought 2013)
Capacity: Max. 16 People (Incl. Crew)
Max speed: 40 Knot / 74 Km/hour
GPS / Sonar: Pelcorn RM-42TX
Tankage: 300 Liter
Lighting: LED / Halogen

Price 99.000 USD
Nice to have
• Big FOR SALE banner on the poster

```html
<!DOCTYPE html>
<html lang="en">
<head>
<meta charset="utf-8">
<title>Speed Boat For Sale</title>
<link rel="stylesheet" href="https://fonts.googleapis.com/css2?family=Sniglet:wght@400;800&family=Kaushan+Script&family=Kalam:wght@700&family=Gelasio:ital@0;1&display=swap">
<style>
  :root {
    --yellow-light: #f4ee62;
    --yellow: #f1d524;
    --orange: #f0a21a;
    --orange-deep: #e9741a;
    --ink: #1d1a10;
    --white: #ffffff;
    --tag-red: #d9161c;
    --tag-red-dark: #a80d12;
    --sky: #8fd6f4;
    --sea: #37c0df;
    --sea-deep: #1b8cbc;
    --palm: #3d8a3a;
    --rock: #b89660;
    --cabin-white: #eef0ef;
    --cabin-beige: #d9c7a3;
  }
  html, body { margin: 0; padding: 0; overflow: hidden; }
  body { width: 900px; height: 1200px; }
  .poster {
    position: relative;
    width: 900px;
    height: 1200px;
    overflow: hidden;
    background:
      radial-gradient(ellipse at 50% 45%, rgba(255,255,200,0.35), transparent 60%),
      linear-gradient(180deg, var(--yellow) 0%, var(--yellow-light) 10%, var(--yellow-light) 45%, var(--yellow) 65%, var(--orange) 85%, var(--orange-deep) 100%);
    font-family: "Kalam", cursive;
    color: var(--ink);
  }
  .poster-title {
    position: absolute;
    top: 38px; left: 0; width: 900px;
    margin: 0;
    text-align: center;
    font-family: "Sniglet", sans-serif;
    font-weight: 400;
    font-size: 72px;
    line-height: 100px;
    letter-spacing: 1px;
    color: var(--white);
    -webkit-text-stroke: 2px var(--ink);
    paint-order: stroke fill;
  }
  .poster-title .emphasis { font-weight: 800; font-size: 92px; }
  .hero-band { position: absolute; top: 145px; left: 0; width: 900px; height: 325px; }
  .interior-photo {
    position: absolute;
    background: linear-gradient(160deg, var(--cabin-white) 0%, #dfe2e1 50%, var(--cabin-beige) 100%);
    border: 4px solid var(--white);
    box-shadow: 2px 3px 8px rgba(0,0,0,0.35);
  }
  .interior-photo.cockpit { left: 412px; top: 515px; width: 268px; height: 150px; transform: rotate(3deg); }
  .interior-photo.cabin { left: 690px; top: 498px; width: 180px; height: 262px; transform: rotate(-8deg); }
  .interior-photo.seating { left: 448px; top: 662px; width: 266px; height: 168px; transform: rotate(2deg); }
  .sale-heading {
    position: absolute; left: 42px; top: 520px; margin: 0;
    font-family: "Kaushan Script", cursive; font-weight: 400; font-size: 34px; letter-spacing: 2px;
  }
  .sale-copy {
    position: absolute; left: 45px; top: 596px; width: 345px;
    font-size: 13px; font-weight: 700; font-style: italic; line-height: 23px;
  }
  .sale-copy p { margin: 0 0 23px; }
  .specs { position: absolute; left: 458px; top: 893px; width: 420px; }
  .specs-heading {
    display: flex; align-items: center; gap: 24px; margin: 0 0 20px;
    font-family: "Sniglet", sans-serif; font-weight: 800; font-size: 18px;
    letter-spacing: 1px;
  }
  .specs-list { margin: 0 0 0 4px; padding: 0; font-family: "Gelasio", serif; font-size: 15px; line-height: 23.5px; }
  .specs-list dt { display: inline; font-style: italic; }
  .specs-list dd { display: inline; margin: 0; }
  .price-tag { position: absolute; left: 0; top: 1025px; width: 420px; height: 175px; }
  .price-label, .price-value { font-family: "Sniglet", sans-serif; font-weight: 800; }
  .island-mark {
    position: absolute; left: 790px; top: 1085px; width: 90px; height: 95px;
    background: radial-gradient(ellipse at 50% 100%, var(--ink) 0 45%, transparent 46%);
  }
</style>
</head>
<body>
<main class="poster">
  <h1 class="poster-title">SPEED BOAT FOR <span class="emphasis">SALE</span></h1>

  <svg class="hero-band" viewBox="0 0 900 325" role="img" aria-label="Photo of the white speed boat anchored in a turquoise tropical lagoon with rocks and palm trees">
    <defs>
      <linearGradient id="heroFill" x1="0" y1="0" x2="0" y2="1">
        <stop offset="0" stop-color="var(--sky)"/>
        <stop offset="0.4" stop-color="#c4ecf8"/>
        <stop offset="0.6" stop-color="var(--sea)"/>
        <stop offset="1" stop-color="var(--sea-deep)"/>
      </linearGradient>
      <radialGradient id="leftShade" cx="0.05" cy="0.55" r="0.35">
        <stop offset="0" stop-color="var(--palm)" stop-opacity="0.55"/>
        <stop offset="1" stop-color="var(--palm)" stop-opacity="0"/>
      </radialGradient>
      <radialGradient id="rightShade" cx="0.92" cy="0.45" r="0.3">
        <stop offset="0" stop-color="var(--palm)" stop-opacity="0.5"/>
        <stop offset="1" stop-color="var(--palm)" stop-opacity="0"/>
      </radialGradient>
      <radialGradient id="rockShade" cx="0.25" cy="0.75" r="0.18">
        <stop offset="0" stop-color="var(--rock)" stop-opacity="0.6"/>
        <stop offset="1" stop-color="var(--rock)" stop-opacity="0"/>
      </radialGradient>
      <clipPath id="heroClip">
        <path d="M0 36 C 250 5, 520 5, 700 16 C 800 24, 860 38, 900 58 L 900 278 C 700 243, 500 243, 300 278 C 180 298, 80 308, 0 297 Z"/>
      </clipPath>
    </defs>
    <path d="M0 28 C 250 -5, 520 -5, 700 8 C 800 16, 860 30, 900 50 L 900 285 C 700 250, 500 250, 300 285 C 180 305, 80 315, 0 305 Z" fill="var(--white)"/>
    <g clip-path="url(#heroClip)">
      <rect width="900" height="325" fill="url(#heroFill)"/>
      <rect width="900" height="325" fill="url(#leftShade)"/>
      <rect width="900" height="325" fill="url(#rightShade)"/>
      <rect width="900" height="325" fill="url(#rockShade)"/>
    </g>
  </svg>

  <div class="interior-photo cockpit" role="img" aria-label="Photo of the cockpit with beige bench seats and helm"></div>
  <div class="interior-photo cabin" role="img" aria-label="Photo of the small cabin with bed and skylight"></div>
  <div class="interior-photo seating" role="img" aria-label="Photo of the open deck seating rows"></div>

  <h2 class="sale-heading">Speed Boat sale</h2>
  <div class="sale-copy">
    <p>This beautiful full glass fiber speed boat (location Lombok, Indonesia) is perfect for tropical conditions. Island transfer, diving, wake boarding, fishing, private charters and leisure features.</p>
    <p>The new (2013) bought 2x 200 HP TORUMI 4 Stroke will give you an enormous power on the water with maximum speed of 40 Knot / 74 Km/hour and will bring you within only 50 minutes from Lombok to Bali and within minute distance from all famous tropical Gili islands.</p>
    <p>The speed boat also has the comfort of a small cabin with skylight, sun controlled ventilation system, a small bed, a toilet and a fridge. In the open section of the boat are 16 seats, besides all of this is the boat equipped with brand-new GPS, Sonar and an FM / AM Radio system.</p>
    <p>This boat was built in 2011 and it was meticulously maintained to the highest standard.</p>
  </div>

  <section class="specs">
    <h3 class="specs-heading">
      <svg width="18" height="14" viewBox="0 0 18 14" aria-hidden="true"><rect x="1" y="1" width="12" height="12" fill="none" stroke="var(--ink)" stroke-width="2"/><path d="M4 6 L7 9 L17 1" fill="none" stroke="var(--ink)" stroke-width="2"/></svg>
      specifications:
    </h3>
    <dl class="specs-list">
      <div><dt>Overall length:</dt> <dd>11 Meter 36 feet.</dd></div>
      <div><dt>Built year:</dt> <dd>2011, Bali</dd></div>
      <div><dt>Engines:</dt> <dd>2x 200 HP TORUMI 4 Stroke (Bought 2013)</dd></div>
      <div><dt>Capacity:</dt> <dd>Max. 16 People (Incl. Crew)</dd></div>
      <div><dt>Max speed:</dt> <dd>40 Knot / 74 Km/hour</dd></div>
      <div><dt>GPS / Sonar:</dt> <dd>Pelcorn RM-42TX</dd></div>
      <div><dt>Tankage:</dt> <dd>300 Liter</dd></div>
      <div><dt>Lighting:</dt> <dd>LED / Halogen</dd></div>
    </dl>
  </section>

  <svg class="price-tag" viewBox="0 0 420 175" aria-label="Price 99,000 dollars">
    <path d="M190 90 C 120 70, 30 20, 22 50 C 15 80, 140 95, 195 92" fill="none" stroke="var(--white)" stroke-width="2.5"/>
    <g transform="rotate(-8 290 100)">
      <path d="M172 70 L 210 42 L 405 42 L 405 158 L 210 158 L 172 130 Z" fill="var(--tag-red)" stroke="var(--tag-red-dark)" stroke-width="2"/>
      <circle cx="198" cy="100" r="14" fill="var(--white)"/>
      <circle cx="198" cy="100" r="7" fill="var(--tag-red-dark)"/>
      <text class="price-label" x="312" y="90" text-anchor="middle" font-size="32" fill="var(--white)">PRICE</text>
      <rect x="228" y="104" width="168" height="40" fill="var(--white)"/>
      <text class="price-value" x="312" y="136" text-anchor="middle" font-size="30" fill="var(--ink)">99,000 $</text>
    </g>
  </svg>

  <div class="island-mark" role="img" aria-label="Small palm island silhouette"></div>
</main>
</body>
</html>
```